Business card design reauest

2 sided. White on both sides

Martin Oakhurst

Ho Chi Minh, Vietnam

Cell Phone / Whatsapp/ Wechat/Zalo
1-555-382-7194
Moakhurst@kvpartsline.vn
Www.kvpartsline.vn
Www.kvpartsline.com

Industry/Entity Type

Sofa and furniture and kitchen

Contact Information for Business Card

2 sided. White on both sides Martin Oakhurst Ho Chi Minh, Vietnam Cell Phone / Whatsapp/ Wechat/Zalo 1-555-382-7194 Moakhurst@kvpartsline.vn Www.kvpartsline.vn Www.kvpartsline.com

```html
<!DOCTYPE html>
<html lang="en">
<head>
<meta charset="utf-8">
<title>KV Partsline – Business Card</title>
<link rel="stylesheet" href="https://fonts.googleapis.com/css2?family=EB+Garamond:wght@400;500;600&display=swap">
<style>
  :root {
    --backdrop: #ebeae7;
    --card: #ffffff;
    --brand-green: #039732;
    --ink: #111111;
    --icon-bg: #ffffff;
  }
  * { box-sizing: border-box; margin: 0; padding: 0; }
  html, body {
    width: 1181px; height: 1200px; overflow: hidden;
    background: var(--backdrop);
    font-family: "EB Garamond", Garamond, Georgia, serif;
    color: var(--ink);
  }
  .card {
    position: absolute; left: 218px;
    width: 746px; height: 426px;
    background: var(--card);
    box-shadow: 0 6px 18px rgba(0,0,0,0.12);
    overflow: hidden;
  }
  .card--front { top: 128px; }
  .card--back { top: 655px; }

  .front-panel {
    position: absolute; left: 0; top: 0;
    width: 368px; height: 426px;
  }
  .front-panel svg { display: block; }

  .holder {
    position: absolute; left: 41px; top: 0; width: 320px;
  }
  .holder__name {
    position: absolute; top: 118px;
    font-size: 44px; font-weight: 400; line-height: 1; white-space: nowrap;
  }
  .holder__location {
    position: absolute; top: 178px;
    font-size: 18px; letter-spacing: 0.09em; color: #ffffff; white-space: nowrap;
  }
  .holder__rule {
    position: absolute; top: 227px; width: 58px; height: 1.5px; background: var(--ink);
  }

  .contacts { position: absolute; left: 33px; top: 264px; list-style: none; }
  .contacts__item {
    display: flex; align-items: center; height: 26px; margin-bottom: 17px;
    font-size: 22px; white-space: nowrap;
  }
  .contacts__icon {
    width: 26px; height: 26px; border-radius: 50%;
    background: var(--icon-bg); flex: none; margin-right: 20px;
    display: flex; align-items: center; justify-content: center;
  }

  .brand-name {
    position: absolute; color: var(--brand-green);
    font-weight: 500; letter-spacing: 0.02em; white-space: nowrap; text-align: center;
  }
  .card--front .brand-name {
    left: 368px; width: 378px; top: 235px; font-size: 32px;
  }
  .card--back .brand-name {
    left: 0; width: 746px; top: 160px; font-size: 54px;
  }
  .back-url {
    position: absolute; left: 0; width: 746px; top: 356px;
    text-align: center; font-size: 25px; font-weight: 600; letter-spacing: 0.5em;
    padding-left: 0.5em;
  }
</style>
</head>
<body>
  <section class="card card--front">
    <div class="front-panel">
      <svg width="368" height="426" viewBox="0 0 368 426" aria-hidden="true">
        <polygon points="0,87 184,0 368,87 368,426 0,426" fill="var(--brand-green)"/>
      </svg>
    </div>
    <div class="holder">
      <h1 class="holder__name">Martin Oakhurst</h1>
      <p class="holder__location">HO CHI MINH, VIETNAM</p>
      <div class="holder__rule"></div>
    </div>
    <ul class="contacts">
      <li class="contacts__item">
        <span class="contacts__icon">
          <svg width="16" height="16" viewBox="0 0 24 24"><path d="M6.6 10.8c1.4 2.8 3.8 5.1 6.6 6.6l2.2-2.2c.3-.3.7-.4 1-.2 1.1.4 2.3.6 3.6.6.6 0 1 .4 1 1V20c0 .6-.4 1-1 1C10.6 21 3 13.4 3 4c0-.6.4-1 1-1h3.5c.6 0 1 .4 1 1 0 1.3.2 2.5.6 3.6.1.3 0 .7-.2 1z" fill="#111"/></svg>
        </span>
        (555) 382-7194
      </li>
      <li class="contacts__item">
        <span class="contacts__icon">
          <svg width="15" height="11" viewBox="0 0 15 11"><rect width="15" height="11" fill="#111"/><path d="M0 0l7.5 6L15 0" fill="none" stroke="#fff" stroke-width="1"/></svg>
        </span>
        Moakhurst@kvpartsline.vn
      </li>
      <li class="contacts__item">
        <span class="contacts__icon">
          <svg width="18" height="18" viewBox="0 0 20 20" fill="none" stroke="#111" stroke-width="1.4"><circle cx="10" cy="10" r="8"/><ellipse cx="10" cy="10" rx="3.5" ry="8"/><path d="M2 10h16M3.5 6h13M3.5 14h13"/></svg>
        </span>
        Www.kvpartsline.vn
      </li>
    </ul>
    <p class="brand-name">KV PARTSLINE</p>
  </section>

  <section class="card card--back">
    <p class="brand-name">KV PARTSLINE</p>
    <p class="back-url">Www.kvpartsline.com</p>
  </section>
</body>
</html>
```